"Every Lantern Still Burning" Sermon Series Design

Needing a design for our church's next sermon series titled "Every Lantern Still Burning" where we will discuss the need for unity, diversity, love and clarity. Looking for a 1920 x 1080 (or higher res) editable and layered file (PSD or AI) so that we can reformat the design to work on social, screens, lower thirds and various print and online mediums. We will also need to have access to the font files so that we can make resize and tweak as needed. We like the idea of using a globe or map of the world as the backdrop with the words overtop. Or, the idea of creating a bunch of newspaper clippings (generic, so that they can't actually be read) and making the shape of a heart. See attached examples. This website will give you an idea of our previous sermon series designs so you can have an idea of our style (but, feel free to help us advance the ball on something more aligned with current design trends): https://www.brinmoorfellowship.church/series

Examples use red, but stay away from a ton of red. If you're gonna major in a color, use blue or something in that family.

Must haves:
Title: Every Lantern Still Burning
Tagline : (TBD - use some Lorem Ipsum as a placeholder and we will fill in later)
Our Logo (attached) (small towards bottom is standard - only use solid colors for logo - preferably just solid black or white)

Industry/Entity Type

Church

Font styles to use
Serif
Sans Serif

Requirements
Must have
• Title: Every Lantern Still Burning
Nice to have
• We like the idea of using a globe or map of the world as the backdrop with the words overtop. Or, the idea of creating a bunch of newspaper clippings (generic, so that they can't actually be read) and making the shape of a heart. See attached examples.

If you're gonna major on a color, stick with blue or something close.
Should not have
• Don't use red as the primary color (example we sent has red, but stay away from it)

```html
<!DOCTYPE html>
<html lang="en">
<head>
<meta charset="utf-8">
<title>Every Lantern Still Burning — Sermon Series</title>
<link rel="stylesheet" href="https://fonts.googleapis.com/css2?family=Jost:wght@300;400&family=Lato:wght@400&display=swap">
<style>
  :root {
    --page: #ffffff;
    --blue-glow: #5c9fd9;
    --blue-mid: #4a7fc1;
    --blue-edge: #44638c;
    --ink: #0a0a0a;
    --globe-light: #62a6de;
    --globe-dark: #2a3a47;
  }
  html, body {
    margin: 0;
    padding: 0;
    width: 1200px;
    height: 796px;
    overflow: hidden;
    background: var(--page);
  }
  .canvas {
    position: relative;
    width: 1200px;
    height: 796px;
    background: var(--page);
  }
  .series-panel {
    position: absolute;
    left: 139px;
    top: 139px;
    width: 923px;
    height: 519px;
    overflow: hidden;
    background:
      radial-gradient(ellipse 60% 70% at 42% 38%, var(--blue-glow) 0%, var(--blue-mid) 60%, transparent 100%),
      radial-gradient(ellipse at center, var(--blue-mid) 45%, var(--blue-edge) 100%);
    box-shadow: inset 0 0 0 1px rgba(40, 60, 90, 0.6);
  }
  .globe {
    position: absolute;
    left: 310px;
    top: 151px;
    width: 152px;
    height: 152px;
    border-radius: 50%;
    background: radial-gradient(circle at 45% 55%, var(--globe-light) 0%, #4f8cc6 55%, var(--globe-dark) 100%);
    box-shadow: 0 8px 18px rgba(20, 40, 70, 0.45);
  }
  .title {
    position: absolute;
    left: 0;
    width: 100%;
    margin: 0;
    text-align: center;
    font-family: "Jost", sans-serif;
    color: var(--ink);
    text-transform: uppercase;
    line-height: 1;
  }
  .title-lead {
    top: 95px;
    font-size: 54px;
    font-weight: 400;
    letter-spacing: 0.16em;
    padding-left: 0.16em;
  }
  .title-hero {
    top: 140px;
    font-size: 188px;
    font-weight: 300;
    letter-spacing: 0.02em;
  }
  .title-close {
    top: 317px;
    font-size: 54px;
    font-weight: 400;
    letter-spacing: 0.2em;
    padding-left: 0.2em;
  }
  .tagline {
    position: absolute;
    left: 0;
    top: 380px;
    width: 100%;
    margin: 0;
    text-align: center;
    font-family: "Lato", sans-serif;
    font-size: 16px;
    color: var(--ink);
  }
  .church-mark {
    position: absolute;
    left: 0;
    top: 452px;
    width: 100%;
    display: flex;
    justify-content: center;
    align-items: center;
    gap: 8px;
    font-family: "Lato", sans-serif;
    font-size: 14px;
    color: var(--ink);
  }
  .church-mark-dot {
    width: 16px;
    height: 16px;
    border-radius: 50%;
    border: 2px solid var(--ink);
    box-sizing: border-box;
  }
</style>
</head>
<body>
  <main class="canvas">
    <section class="series-panel">
      <div class="globe" role="img" aria-label="Globe of the Earth showing Europe and Africa in dark tones"></div>
      <h1 class="title title-lead">Every Lantern</h1>
      <p class="title title-hero">Still</p>
      <p class="title title-close">Burning</p>
      <p class="tagline">Lorem ipsum dolor sit amet, consectetuer adipiscing elit, sed diam</p>
      <div class="church-mark">
        <span class="church-mark-dot"></span>
        <span class="church-mark-name">Brinmoor Fellowship</span>
      </div>
    </section>
  </main>
</body>
</html>
```